Business Card for Brightmoor Holdings

I am looking for a design for my business card. I need a logo. The company is called Brightmoor Holdings. We are an investment management and technology consulting company. I am looking for a professional conservative design. I think a lighthouse might be a good simple for us.

For the business card.
company URL www.brightmoorholdings.example
my name: Calvin R. Pratt
email: cpratt@brightmoorholdings.example
my phone # 555-301-6947

Contact Information for Business Card

company URL www.brightmoorholdings.example my name: Calvin R. Pratt email: cpratt@brightmoorholdings.example my phone # 555-301-6947

Colors
0054AA
0677BA
7BADD7
CADEEF
E8F1F8

Requirements
Must have
• area on the back for a QR code

```html
<!DOCTYPE html>
<html lang="en">
<head>
<meta charset="utf-8">
<title>Brightmoor Holdings — Business Card</title>
<link href="https://fonts.googleapis.com/css2?family=Montserrat:wght@400;500;700&display=swap" rel="stylesheet">
<style>
  :root {
    --navy: #0b3f78;
    --navy-deep: #083766;
    --gold: #f0c230;
    --paper: #ffffff;
    --ink: #1c1c1c;
    --muted: #3a3a3a;
    --backdrop: #e9ebee;
    --qr-border: #7badd7;
  }
  * { box-sizing: border-box; margin: 0; padding: 0; }
  html, body {
    width: 1200px; height: 1200px; overflow: hidden;
    background: var(--backdrop);
    font-family: "Montserrat", sans-serif;
  }
  .sheet {
    position: relative; width: 1200px; height: 1200px;
    display: flex; flex-direction: column; align-items: center; justify-content: center; gap: 60px;
  }
  .card {
    position: relative; width: 840px; height: 480px;
    border-radius: 34px; overflow: hidden;
    box-shadow: 0 10px 28px rgba(0,0,0,0.18);
  }
  .card--front { background: var(--paper); }
  .card--back { background: var(--navy-deep); }

  .edge-bands { position: absolute; left: 0; bottom: 0; width: 840px; height: 120px; }

  .contact { position: absolute; left: 64px; top: 190px; }
  .contact__name {
    color: var(--navy); font-weight: 700; font-size: 30px;
    letter-spacing: 0.5px; text-transform: uppercase; line-height: 1;
  }
  .contact__title { color: var(--muted); font-size: 22px; margin-top: 4px; }
  .contact__list { list-style: none; margin-top: 26px; }
  .contact__item {
    display: flex; align-items: center; gap: 14px;
    color: var(--ink); font-size: 18px; line-height: 1.6;
  }
  .contact__icon { width: 22px; height: 22px; flex: none; fill: var(--navy); }
  .contact__icon--outline { fill: none; stroke: var(--navy); stroke-width: 1.8; }

  .brand { position: absolute; display: flex; align-items: center; gap: 16px; }
  .brand__mark { width: 46px; height: 46px; flex: none; }
  .brand__name { font-weight: 700; font-size: 34px; letter-spacing: 1px; text-transform: uppercase; line-height: 1.05; }
  .card--front .brand { left: 500px; top: 120px; }
  .card--front .brand__mark { background: var(--navy); }
  .card--front .brand__name { color: var(--navy); }
  .card--back .brand { left: 190px; top: 50%; transform: translateY(-50%); gap: 22px; }
  .card--back .brand__mark { width: 64px; height: 64px; background: var(--paper); }
  .card--back .brand__name { color: var(--paper); font-size: 44px; }

  .qr-area {
    position: absolute; right: 48px; bottom: 48px;
    width: 120px; height: 120px; border-radius: 10px;
    background: var(--paper); border: 3px solid var(--qr-border);
  }
</style>
</head>
<body>
<main class="sheet">
  <section class="card card--front" aria-label="Business card front">
    <div class="brand">
      <span class="brand__mark"></span>
      <span class="brand__name">Brightmoor<br>Holdings</span>
    </div>

    <div class="contact">
      <p class="contact__name">Calvin R. Pratt</p>
      <p class="contact__title">CEO</p>
      <ul class="contact__list">
        <li class="contact__item">
          <svg class="contact__icon" viewBox="0 0 24 24"><path d="M6.6 10.8c1.4 2.8 3.8 5.1 6.6 6.6l2.2-2.2c.3-.3.7-.4 1-.2 1.1.4 2.3.6 3.6.6.6 0 1 .4 1 1V20c0 .6-.4 1-1 1C10.6 21 3 13.4 3 4c0-.6.4-1 1-1h3.5c.6 0 1 .4 1 1 0 1.3.2 2.5.6 3.6.1.3 0 .7-.2 1z"/></svg>
          555-301-6947
        </li>
        <li class="contact__item">
          <svg class="contact__icon" viewBox="0 0 24 24"><path d="M2 5h20v14H2z M4 7v.5l8 5.5 8-5.5V7l-8 5.5z" fill-rule="evenodd"/></svg>
          cpratt@brightmoorholdings.example
        </li>
        <li class="contact__item">
          <svg class="contact__icon contact__icon--outline" viewBox="0 0 24 24"><circle cx="12" cy="12" r="9.5"/><ellipse cx="12" cy="12" rx="4" ry="9.5"/><path d="M2.5 12h19M4 7h16M4 17h16"/></svg>
          www.brightmoorholdings.example
        </li>
      </ul>
    </div>

    <svg class="edge-bands" viewBox="0 0 840 120" preserveAspectRatio="none" aria-hidden="true">
      <polygon points="0,102 540,102 552,84 552,120 0,120" fill="var(--navy)"/>
      <polygon points="562,84 840,84 840,120 562,120" fill="var(--gold)"/>
      <polygon points="562,84 574,84 562,102" fill="var(--paper)"/>
    </svg>
  </section>

  <section class="card card--back" aria-label="Business card back">
    <div class="brand">
      <span class="brand__mark"></span>
      <span class="brand__name">Brightmoor<br>Holdings</span>
    </div>
    <div class="qr-area" role="img" aria-label="Reserved area for QR code"></div>
  </section>
</main>
</body>
</html>
```